New travel store signage for Kelvane Journeys to attract luxury travellers.

Hello,
We are looking to change the signage of our stores. The signage must include the following:
1. Kelvane Journeys Logo (attached)
2. The text...The Travel & Cruise Experts
3. Brand Colours ( Fb0196, 412266, d41d84 and ffffff)
Please note the signage design must be central and only cover two thirds of the store front. We have also attached an image of one of our new stores which might be helpful when preparing a mock up.

We are looking for a quick turnaround on this, making a decision within 48 hours.

Target Market(s)

Retail

Industry/Entity Type

Travel Agency

Font styles to use
Other font styles liked:
• Radley

Colors
E54698
E96AAD
F1A4CE
F9D9EA
FCEFF6
6B429C
8869AF
B7A5CE
E3DAEB
F3F0F8

Requirements
Must have
• Hello, We are looking to change the signage of our stores. The signage must include the following: 1. Kelvane Journeys Logo (attached) 2. The text...The Travel & Cruise Experts 3. Brand Colours ( Fb0196, 412266, d41d84 and ffffff) Please note the signage design must be central and only cover two thirds of the store front.
Should not have
• different colour or fonts. Gradient design.

```html
<!DOCTYPE html>
<html lang="en">
<head>
<meta charset="utf-8">
<title>Kelvane Journeys – Store Signage</title>
<link href="https://fonts.googleapis.com/css2?family=Montserrat:ital,wght@0,500;0,600;1,500&display=swap" rel="stylesheet">
<style>
  :root {
    --stage: #b3b3b3;
    --white: #ffffff;
    --pink: #e91e8c;
    --navy: #272160;
  }
  * { margin: 0; padding: 0; box-sizing: border-box; }
  html, body { width: 1200px; height: 1020px; overflow: hidden; background: var(--stage); }
  body { position: relative; font-family: "Montserrat", Arial, sans-serif; }

  .sign { position: absolute; background: var(--white); overflow: hidden; }
  .sign-wave { position: absolute; inset: 0; width: 100%; height: 100%; }

  .fascia { left: 20px; top: 203px; width: 1161px; height: 275px; }
  .fascia .brand { left: 530px; top: 122px; }
  .fascia .brand-name { font-size: 44px; }
  .fascia .brand-dot { width: 26px; height: 26px; }
  .tagline {
    position: absolute; left: 82px; top: 225px;
    color: var(--white); font-size: 25px; font-style: italic; font-weight: 500;
    letter-spacing: 0.3px;
  }

  .card { left: 338px; top: 623px; width: 540px; height: 300px; }
  .card .brand { left: 170px; top: 112px; }
  .card .brand-name { font-size: 27px; }
  .card .brand-dot { width: 17px; height: 17px; }

  .brand { position: absolute; display: flex; align-items: center; gap: 12px; white-space: nowrap; }
  .brand-dot { border-radius: 50%; background: var(--pink); flex: none; }
  .brand-name { color: var(--navy); font-weight: 600; line-height: 1; }

  .contact { position: absolute; left: 72px; top: 232px; color: var(--white); font-weight: 500; }
  .contact-phone { display: flex; align-items: center; gap: 6px; margin-left: 16px; font-size: 20px; line-height: 1; }
  .phone-icon { width: 22px; height: 22px; flex: none; }
  .contact-web { margin-top: 6px; font-size: 18px; line-height: 1; }
  .contact-web .accent { color: var(--pink); }
</style>
</head>
<body>

<section class="sign fascia">
  <svg class="sign-wave" viewBox="0 0 1935 459" preserveAspectRatio="none" aria-hidden="true">
    <path fill="var(--pink)" d="M0,287 C250,250 500,300 800,350 C1100,400 1300,410 1500,405 C1700,400 1850,290 1935,165 L1935,459 L0,459Z"/>
    <path fill="var(--white)" d="M0,335 C250,295 500,330 800,375 C1100,420 1300,428 1500,423 C1700,418 1850,340 1935,255 L1935,459 L0,459Z"/>
    <path fill="var(--navy)" d="M0,362 C250,315 500,345 800,388 C1100,432 1300,445 1500,440 C1700,435 1850,360 1935,280 L1935,459 L0,459Z"/>
  </svg>
  <div class="brand">
    <span class="brand-dot"></span>
    <span class="brand-name">Kelvane Journeys</span>
  </div>
  <p class="tagline">The Travel &amp; Cruise Experts</p>
</section>

<section class="sign card">
  <svg class="sign-wave" viewBox="0 0 900 499" preserveAspectRatio="none" aria-hidden="true">
    <path fill="var(--pink)" d="M0,311 C200,300 500,335 900,402 L900,499 L0,499Z"/>
    <path fill="var(--white)" d="M0,350 C200,335 500,362 900,416 L900,499 L0,499Z"/>
    <path fill="var(--navy)" d="M0,374 C200,345 500,372 900,432 L900,499 L0,499Z"/>
  </svg>
  <div class="brand">
    <span class="brand-dot"></span>
    <span class="brand-name">Kelvane Journeys</span>
  </div>
  <div class="contact">
    <p class="contact-phone">
      <svg class="phone-icon" viewBox="0 0 24 24" aria-hidden="true">
        <circle cx="12" cy="12" r="12" fill="var(--pink)"/>
        <path fill="var(--navy)" d="M8.3 6.2c.4-.3 1-.2 1.3.2l1.3 2c.3.4.2.9-.1 1.2l-.9.8c.6 1.3 1.6 2.4 2.9 3.1l.8-.9c.3-.4.9-.4 1.2-.1l2 1.3c.4.3.5.9.2 1.3l-.8 1.1c-.4.5-1 .7-1.6.5-3.4-1-6-3.7-7-7.1-.2-.6 0-1.2.5-1.6z"/>
      </svg>
      0300 555 0142
    </p>
    <p class="contact-web">www.<span class="accent">kelvanejourneys</span>.com</p>
  </div>
</section>

</body>
</html>
```